Stationery Design Project

We need a stationery design for our Norwegian trucking company. We have existed for about 15 years and our 12 drivers uses relatively new vehicles to transport goods around in northern Norway. Long distance routes with fresh fish og food transport is our main operations.

We have already made alogo that's printed on our trucks. The logo and a picture of our trucks is attached. I think the logo i crappy, but since its already in use, changing it is not an option in this round. Still using a better colour scheme in the overall stationery and more interesting fonts is possible (altso in the logo).

Company details:
Name: Vikstrandbil AS
Organisation nr 981 537 608
Post adress: 8613 Lysvær

I like minimalism and simplicity. I am avalibly for questions in normal GMT working hours either here or on mail: petter@vikstrand.no

Reason: Hi. Im extending the deadline because I needed some time to find a vector file of our logo. Sorry for the inconvenience

Hi, and thanks for all your interest in the project. Some updates:

-          I have decided to commit to using one of the designs. Some designer will get the payment.

-          I have extended the deadline with 24 hours since I needed some time to find our firms vector logo (a slow Swedish man was holding me up)

-          We will not choose a design before the deadline. No need to rush.

-          We have received a lot of great design and think there is a need to specified the product we want to make:

o   Business Card for all our employers. I just need the design and will duplicate with the correct numbers and name myself. The information on should be: Logo, employer’s name, Phone number, email, website, Postal number and address. Use this as a template: logo, Leif Brattli, 47283916, Leif@vikstrand.no,, vikstrand.no, 8613 Lysvær. The order and placement of the information is your creative decision.

o   Stickers to put on the goods we travel. On the sticker the should be the following information: Logo, phone number, Tekst and link: Fraktæ av Vikstrandbil. Ke du syns? Vikstrand.no/tilbakemelding (this means: Handled by Vikstrandbil. What do you think Vikstrand.no/feedback -à the link will be a feedback form). The placement the information and size is your creative decision with some stings: we have been thinking of using Prentavo for printing and see that a size about 6x6 cm, 8x5 or something like that. (with 3000 copies our budget is 200 punds). Any suggestions of other suppliers are welcome. Prentavo price calculator http://www.prentavoprint.co.uk/digital-litho-printing/printing-labels-tags/stickers/

o   Letterhead with logo, address, phone number and organizational number.

o   Envelopes with logo,address, phone number and organizational number.

Have a nice day.

 

 

• Using the blue colour in the logo and using a similar graphic approch.

```html
<!DOCTYPE html>
<html lang="no">
<head>
<meta charset="utf-8">
<title>Vikstrandbil – stationery</title>
<link rel="stylesheet" href="https://fonts.googleapis.com/css2?family=Crimson+Text:wght@400;700&display=swap">
<style>
  :root {
    --backdrop: #1d4f6e;
    --navy: #2b2577;
    --ocean: #0a5a9c;
    --sky: #5fb0e0;
    --ice: #9cc3e6;
    --paper: #ffffff;
    --link-blue: #4a9bd4;
    --photo-dusk: linear-gradient(180deg, #a9b7c8 0%, #6d7f95 100%);
    --photo-coast: linear-gradient(180deg, #c9a98a 0%, #5b6f78 100%);
  }
  * { box-sizing: border-box; margin: 0; padding: 0; }
  html, body { width: 1200px; height: 900px; overflow: hidden; }
  body {
    position: relative;
    background: var(--backdrop);
    font-family: "Crimson Text", "Times New Roman", serif;
    color: var(--navy);
  }
  .brand-name {
    font-family: "Crimson Text", serif;
    font-weight: 700;
    color: var(--navy);
    white-space: nowrap;
  }

  /* Letterhead */
  .letterhead {
    position: absolute; left: 556px; top: 113px;
    width: 454px; height: 642px;
    background: var(--paper);
  }
  .letterhead__tiles {
    position: absolute; left: 8px; top: 8px;
    display: grid;
    grid-template-columns: repeat(7, 60px);
    grid-template-rows: repeat(3, 40px);
    gap: 3px;
  }
  .tile { border-radius: 5px; }
  .tile--navy { background: var(--navy); }
  .tile--ocean { background: var(--ocean); }
  .tile--sky { background: var(--sky); }
  .tile--ice { background: var(--ice); }
  .tile--photo-dusk { background: var(--photo-dusk); }
  .tile--photo-coast { background: var(--photo-coast); }
  .tile--brand {
    grid-column: span 2;
    display: flex; align-items: center; justify-content: center;
    font-size: 19px;
  }
  .letterhead__footer {
    position: absolute; left: 0; bottom: 0;
    width: 100%; height: 43px;
    background: var(--navy);
    color: var(--paper);
    font-weight: 700; font-size: 13px; line-height: 17px;
    text-align: center;
    padding-top: 5px;
  }

  /* Envelope */
  .envelope {
    position: absolute; left: 160px; top: 452px;
    width: 475px; height: 238px;
    background: var(--paper);
  }
  .envelope__tiles {
    position: absolute; left: 3px; top: 5px;
    display: grid;
    grid-template-columns: repeat(16, 27px);
    grid-template-rows: 17px;
    gap: 2.5px;
  }
  .envelope__tiles .tile { border-radius: 2px; }
  .envelope__brand {
    position: absolute; left: 30px; top: 46px;
    font-size: 20px;
  }
  .envelope__contact {
    position: absolute; left: 30px; top: 78px;
    font-size: 8px; line-height: 9px;
    color: var(--link-blue);
  }
  .envelope__window {
    position: absolute; left: 240px; top: 102px;
    width: 174px; height: 87px;
    border: 1.5px solid var(--link-blue);
    border-radius: 8px;
  }
  .envelope__band {
    position: absolute; left: 0; bottom: 0;
    width: 100%; height: 22px;
    background: var(--navy);
  }

  /* Business card */
  .business-card {
    position: absolute; left: 312px; top: 236px;
    width: 192px; height: 112px;
    background: var(--paper);
  }
  .business-card__tiles {
    position: absolute; right: 4px; top: 4px;
    display: grid;
    grid-template-columns: repeat(4, 24px);
    grid-template-rows: 16px;
    gap: 2px;
  }
  .business-card__tiles .tile { border-radius: 2px; }
  .business-card__brand {
    position: absolute; left: 6px; top: 6px;
    font-size: 9px; line-height: 12px;
  }
  .business-card__details {
    position: absolute; left: 0; top: 32px; width: 100%;
    text-align: center;
    font-size: 7px; line-height: 8px;
    color: #222;
  }
  .business-card__name {
    font-size: 10px; font-weight: 700; line-height: 12px;
  }
  .business-card__band {
    position: absolute; left: 0; bottom: 0;
    width: 100%; height: 9px;
    background: var(--navy);
  }

  /* Sticker */
  .sticker {
    position: absolute; left: 485px; top: 323px;
    width: 86px; height: 88px;
    background: var(--navy);
    border-radius: 8px;
    color: var(--paper);
    text-align: center;
    padding-top: 5px;
  }
  .sticker__brand {
    display: inline-block;
    background: var(--paper);
    border-radius: 5px;
    padding: 1px 5px;
    font-size: 9px;
  }
  .sticker__phone {
    font-size: 8px; font-weight: 700; margin-top: 5px;
  }
  .sticker__message {
    font-size: 6px; font-weight: 700; line-height: 8px; margin-top: 3px;
  }
</style>
</head>
<body>

<section class="letterhead" aria-label="Letterhead">
  <div class="letterhead__tiles">
    <div class="tile tile--ocean"></div>
    <div class="tile tile--photo-dusk" role="img" aria-label="Photo of a truck on a snowy winter road"></div>
    <div class="tile tile--sky"></div>
    <div class="tile tile--ice"></div>
    <div class="tile tile--navy"></div>
    <div class="tile tile--ocean"></div>
    <div class="tile tile--photo-dusk" role="img" aria-label="Photo of a snowy northern landscape"></div>

    <div class="tile tile--navy"></div>
    <div class="tile tile--ice"></div>
    <div class="tile tile--navy"></div>
    <div class="tile tile--sky"></div>
    <div class="tile tile--brand"><span class="brand-name">Vikstrandbil</span></div>
    <div class="tile tile--sky"></div>

    <div class="tile tile--photo-coast" role="img" aria-label="Photo of a fjord with mountains"></div>
    <div class="tile tile--sky"></div>
    <div class="tile tile--ocean"></div>
    <div class="tile tile--photo-coast" role="img" aria-label="Photo of a coastal lighthouse at sunset"></div>
    <div class="tile tile--sky"></div>
    <div class="tile tile--ice"></div>
    <div class="tile tile--navy"></div>
  </div>
  <footer class="letterhead__footer">
    <p>Web: www.vikstrand.no &nbsp;|&nbsp; Email: Leif@vikstrand.no</p>
    <p>Telephone: 47283916 &nbsp;|&nbsp; Address: 8613 Lysvær, Norway</p>
  </footer>
</section>

<section class="envelope" aria-label="Envelope">
  <div class="envelope__tiles">
    <div class="tile tile--sky"></div><div class="tile tile--ocean"></div><div class="tile tile--navy"></div><div class="tile tile--ice"></div>
    <div class="tile tile--sky"></div><div class="tile tile--ocean"></div><div class="tile tile--navy"></div><div class="tile tile--ice"></div>
    <div class="tile tile--sky"></div><div class="tile tile--ocean"></div><div class="tile tile--navy"></div><div class="tile tile--ice"></div>
    <div class="tile tile--sky"></div><div class="tile tile--ocean"></div><div class="tile tile--navy"></div><div class="tile tile--ice"></div>
  </div>
  <div class="envelope__brand brand-name">Vikstrandbil</div>
  <div class="envelope__contact">
    <p>www.vikstrand.no &nbsp;|Leif@vikstrand.no</p>
    <p>47283916 &nbsp;|8613 Lysvær, Norway</p>
  </div>
  <div class="envelope__window"></div>
  <div class="envelope__band"></div>
</section>

<section class="business-card" aria-label="Business card">
  <div class="business-card__brand brand-name">Vikstrandbil</div>
  <div class="business-card__tiles">
    <div class="tile tile--ocean"></div><div class="tile tile--navy"></div><div class="tile tile--ice"></div><div class="tile tile--ocean"></div>
  </div>
  <div class="business-card__details">
    <p class="business-card__name">Leif Brattli</p>
    <p>8613 Lysvær</p>
    <p>47283916</p>
    <p>Leif@vikstrand.no</p>
    <p>www.vikstrand.no</p>
  </div>
  <div class="business-card__band"></div>
</section>

<section class="sticker" aria-label="Sticker">
  <span class="sticker__brand brand-name">Vikstrandbil</span>
  <p class="sticker__phone">Tel: 47283916</p>
  <div class="sticker__message">
    <p>Tekst and link:</p>
    <p>Fraktæ av Vikstrandbil.</p>
    <p>Ke du syns?</p>
    <p>Vikstrand.no/tilbakemelding</p>
  </div>
</section>

</body>
</html>
```